Business Card Design

I need a business card design for my law office based in Pasadena, California. I am a sole practitioner and I specialize in business transaction and litigation, probate and estate planning, taxation law, corporate and business formation, immigration and real estate. I want something that is simple, yet stands out.

A friend helped to create a logo about 6 years ago. I am open to new ideas to changing the logo.

Industry/Entity Type

Business

Contact Information for Business Card

Law Offices of Dorvan L. Mabry
842 W. Larkspur Ave., Suite 319
Pasadena, CA 90287
Tel: 626-555-0174
Fax: 626-555-0139
Email: dmabry@dlmlegalgroup.example

Attorney: Dorvan L. Mabry

```html
<!DOCTYPE html>
<html lang="en">
<head>
<meta charset="utf-8">
<title>Law Offices of Dorvan L. Mabry — Business Card</title>
<link rel="stylesheet" href="https://fonts.googleapis.com/css2?family=Cinzel:wght@400;500&family=Crimson+Text:ital,wght@0,400;1,400&display=swap">
<style>
  :root {
    --backdrop: #9b9b9b;
    --paper: #e8e8e9;
    --ink: #1c1c1c;
    --ink-soft: #4a4a4a;
    --band: #1e1e1e;
    --band-tab: #6f6f6f;
    --reverse: #161616;
    --reverse-ink: #ececec;
  }
  * { margin: 0; padding: 0; box-sizing: border-box; }
  html, body {
    width: 1105px; height: 1200px; overflow: hidden;
    background: var(--backdrop);
  }
  .canvas { position: relative; width: 1105px; height: 1200px; }

  .card {
    position: absolute; left: 179px; width: 747px; height: 425px;
    overflow: hidden;
  }
  .card--front { top: 119px; background: var(--paper); }
  .card--back { top: 637px; background: var(--reverse); }

  /* Front: identity block */
  .firm-name {
    position: absolute; left: 60px; top: 128px; width: 350px;
    text-align: center;
    font-family: "Cinzel", serif; font-weight: 400;
    font-size: 26px; line-height: 1.3; color: var(--ink);
  }
  .firm-name__mark {
    display: block; width: 34px; height: 34px;
    margin: 0 auto 16px; background: var(--ink);
  }

  /* Front: contact block */
  .contact {
    position: absolute; left: 421px; top: 78px;
    font-family: "Crimson Text", serif; color: var(--ink-soft);
  }
  .contact__name {
    font-family: "Cinzel", serif; font-weight: 500;
    font-size: 27px; line-height: 1.1; color: var(--ink);
  }
  .contact__title {
    font-family: "Cinzel", serif; font-size: 21px; line-height: 1.2;
    color: var(--ink-soft); margin-bottom: 8px;
  }
  .contact__address { font-size: 20px; line-height: 1.32; font-style: normal; }
  .contact__lines { list-style: none; margin-top: 6px; font-size: 19px; line-height: 1.45; }
  .contact__lines li { display: flex; align-items: center; gap: 9px; }
  .contact__lines svg { width: 15px; height: 15px; fill: var(--ink); flex: none; }

  /* Front: bottom band */
  .web-band {
    position: absolute; left: 0; bottom: 0; width: 100%; height: 28px;
    background: var(--band);
  }
  .web-band__tab {
    position: absolute; left: 184px; bottom: 0; width: 403px; height: 28px;
    background: var(--band-tab);
    clip-path: polygon(18px 0, calc(100% - 18px) 0, 100% 100%, 0 100%);
    display: flex; align-items: center; justify-content: center;
    font-family: "Crimson Text", serif; font-style: italic;
    font-size: 17px; letter-spacing: 3px; color: #f1f1f1;
  }

  /* Back */
  .back-name {
    position: absolute; left: 0; top: 150px; width: 100%;
    text-align: center;
    font-family: "Cinzel", serif; font-weight: 400;
    font-size: 34px; line-height: 1.2; color: var(--reverse-ink);
  }
  .back-name__mark {
    display: block; width: 40px; height: 40px;
    margin: 0 auto 20px; background: var(--reverse-ink);
  }
  .back-web {
    position: absolute; left: 0; top: 352px; width: 100%;
    text-align: center;
    font-family: "Crimson Text", serif; font-size: 21px;
    letter-spacing: 2.5px; color: var(--reverse-ink);
  }
</style>
</head>
<body>
<main class="canvas">

  <section class="card card--front" aria-label="Business card front">
    <div class="firm-name">
      <span class="firm-name__mark" aria-hidden="true"></span>
      Law Offices of<br>Dorvan L. Mabry
    </div>

    <div class="contact">
      <p class="contact__name">Dorvan L. Mabry</p>
      <p class="contact__title">CEO/Founder</p>
      <address class="contact__address">842 W. Larkspur Ave.<br>Suite 319<br>Pasadena, CA 90287</address>
      <ul class="contact__lines">
        <li>
          <svg viewBox="0 0 24 24" aria-label="Phone"><path d="M6.6 10.8a15.1 15.1 0 0 0 6.6 6.6l2.2-2.2c.3-.3.7-.4 1-.2 1.1.4 2.3.6 3.6.6.6 0 1 .4 1 1V20c0 .6-.4 1-1 1A17 17 0 0 1 3 4c0-.6.4-1 1-1h3.5c.6 0 1 .4 1 1 0 1.3.2 2.5.6 3.6.1.3 0 .7-.2 1z"/></svg>
          626-555-0174
        </li>
        <li>
          <svg viewBox="0 0 24 24" aria-label="Fax"><path d="M6 2h12v6H6zM3 9h18a1 1 0 0 1 1 1v8h-4v4H6v-4H2v-8a1 1 0 0 1 1-1zm5 7v4h8v-4z"/></svg>
          626-555-0139
        </li>
        <li>
          <svg viewBox="0 0 24 24" aria-label="Email"><path d="M2 5h20v14H2zm2 2v.4l8 5 8-5V7zm0 2.8V17h16V9.8l-8 5z"/></svg>
          dmabry@dlmlegalgroup.example
        </li>
      </ul>
    </div>

    <div class="web-band">
      <div class="web-band__tab">www.dlmlegalgroup.example</div>
    </div>
  </section>

  <section class="card card--back" aria-label="Business card back">
    <div class="back-name">
      <span class="back-name__mark" aria-hidden="true"></span>
      Dorvan L. Mabry
    </div>
    <p class="back-web">www.dlmlegalgroup.example</p>
  </section>

</main>
</body>
</html>
```